Web Design Project

Hi everyone

Thanks for taking the time to read about this project.

Website needed for Lorel, female singer/songwriter and performer who is launching her debut album this year. She writes and performs folk/pop/soft rock music and plays guitar and piano.

see vidplexa links for examples of Lorel's style:
http://www.vidplexa.com/watch?v=qTbn4Zr8Lp2
http://www.vidplexa.com/watch?v=Kovd7wUheJm

Looking for a classy, modern feel to the website. Cool colours are preferred but open to ideas. It needs it to have CoinDrop set up so items can be purchased from the site. The theme will be continued to Chatterbook and business cards.

Examples include:

http://www.bettyculverdale.com/

http://tessafordyce.com/

http://www.juneqtunes.com/home

Pages and content to be included:

HOME - main picture and general content

BIO - written content about Lorel

NEWS - this will be regularly updated, blog style

GIGS - this will be regularly updated

GALLERY - content will be photos only

SEE AND HEAR - content will be Videos and audios

STORE - this will have a coindrop function for purchase of CD and merchandise

GENEROSITY - this page will be devoted to charity work and updated regularly

CONTACT - information on how to contact Lorel's management

Buttons will need to provide links to Vidplexa, Chirpline, Chatterbook, Snapgrove

I will work closely with the designers in giving feedback as ideas are generated and then provide further content such as photos and videos.

Thanks for considering this project!
Updates

HI everyone thanks for all your submissions so far. Please note the following:

- photos have been uploaded to assist with themes

- background could be a solid colour or texture (e.g. tree trunk texture)

- please use a hand writing font similar to Google font "Give You Glory" - doesn't have to be exactly this but similar

Thank you,

Lorel

Hi again everyone

I apologise but the pixel guild website won't allow me to upload files. I will attempt to correct this as soon as possible. Thanks                                   

18-55 year olds who appreciate this genre of music; gay and lesbian community

Charity

• No flowers or flowery themes

```html
<!DOCTYPE html>
<html lang="en">
<head>
<meta charset="utf-8">
<title>Lorel Halden Official Website</title>
<link href="https://fonts.googleapis.com/css2?family=Ubuntu:wght@400;500&family=Lato:wght@400;700&display=swap" rel="stylesheet">
<style>
:root{
  --red:#c8070e;
  --ink:#4f4f4f;
  --ink-soft:#5e5e5e;
  --brand-dark:#3a3a3a;
  --paper:#f4eae6;
  --white:#ffffff;
  --rule:#e2d2cc;
  --badge:#f1c9b8;
  --footer:#4a4a4a;
  --sky:#7fbfe6;
}
*{margin:0;padding:0;box-sizing:border-box}
html,body{width:900px;height:1200px;overflow:hidden}
body{position:relative;background:var(--paper);font-family:"Lato",sans-serif;color:var(--ink)}
.abs{position:absolute}
.top-rule{left:0;top:0;width:900px;height:3px;background:var(--red)}
.utility-tab{left:490px;top:0;width:312px;height:33px;background:var(--red);
  clip-path:polygon(0 0,100% 0,97% 100%,3% 100%);display:flex;align-items:center;justify-content:center;gap:11px;
  font-family:"Ubuntu",sans-serif;font-size:10px;color:var(--white);padding-top:2px}
.brand{left:97px;top:16px;width:156px;font-family:"Ubuntu",sans-serif;line-height:1}
.brand .first{display:block;font-size:33px;text-align:right;color:var(--brand-dark)}
.brand .last{display:block;font-size:38px;letter-spacing:1px;margin-top:2px;color:var(--red)}
.main-nav{right:98px;top:81px;display:flex;gap:18px;font-family:"Ubuntu",sans-serif;font-size:12px;color:#333}
.hero{left:97px;top:118px;width:706px;height:321px;border:1px solid #ddd;border-radius:8px;background:#f0e6e2;padding:6px}
.hero-stage{position:relative;width:100%;height:100%;border-radius:4px;overflow:hidden;background:#141414}
.hero-portrait{position:absolute;left:0;top:0;width:282px;height:100%;background:linear-gradient(160deg,#6a3f22,#8a5a34 45%,#3a2414)}
.hero-wall{position:absolute;left:282px;top:0;right:0;height:100%;background:linear-gradient(90deg,#202020,#121212)}
.hero-title{position:absolute;left:325px;top:78px;font-family:"Ubuntu",sans-serif;font-weight:400;font-size:29px;line-height:45px;color:var(--white)}
.hero-arrow{position:absolute;top:267px;width:30px;height:30px;border-radius:50%;background:#f2f2f2;border:2px solid #bbb}
.welcome{left:0;top:449px;width:900px;text-align:center;font-family:"Ubuntu",sans-serif;font-weight:400;font-size:31px;color:var(--ink)}
.intro{left:100px;top:497px;width:700px;text-align:center;font-size:9.5px;line-height:17px;color:var(--ink-soft)}
.rule-full{left:0;top:570px;width:900px;height:1px;background:var(--rule)}
.section-head{font-family:"Ubuntu",sans-serif;font-weight:400;font-size:19px;color:var(--red)}
.photo{border-radius:7px}
.blurb{font-size:9.5px;line-height:15px;color:var(--ink-soft);width:172px}
.btn{background:var(--red);color:var(--white);font-family:"Ubuntu",sans-serif;font-size:10px;display:flex;align-items:center;justify-content:center}
.rule-half{height:1px;background:var(--rule);top:725px}
.lower{left:0;top:880px;width:900px;height:237px;background:var(--white)}
.col-head{font-family:"Ubuntu",sans-serif;font-weight:400;font-size:19px;color:var(--ink);top:893px}
.date-badge{width:45px;height:45px;border-radius:7px;background:var(--badge);color:var(--red);text-align:center;font-family:"Ubuntu",sans-serif}
.date-badge .mon{display:block;font-size:11px;margin-top:5px}
.date-badge .day{display:block;font-size:20px;line-height:20px}
.show-text{font-size:9.5px;line-height:15px;width:170px;color:var(--ink)}
.read-more{font-size:9.5px;color:var(--red)}
.tweet-icon{width:30px;height:30px;border-radius:50%;background:var(--sky)}
.tweet{font-size:9.5px;line-height:15px;width:175px;color:var(--ink)}
.tweet a{color:var(--red);text-decoration:none}
.tweet .ago{color:#888}
.social-item .name{font-family:"Ubuntu",sans-serif;font-weight:500;font-size:12px;color:var(--red)}
.social-item .desc{font-size:9.5px;color:var(--ink);margin-top:2px}
.footer{left:0;top:1117px;width:900px;height:83px;background:var(--footer)}
.copyright{left:97px;top:1153px;font-size:8.5px;font-weight:700;color:#d0d0d0}
.social-dot{top:1143px;width:30px;height:30px;border-radius:50%;background:#1e1e1e;border:1px solid #666}
</style>
</head>
<body>
<div class="abs top-rule"></div>
<nav class="abs utility-tab"><span>Join the Mailing List</span><span>|</span><span>Play Music</span><span>|</span><span>Login</span><span>|</span><span>Register</span></nav>

<div class="abs brand"><span class="first">lorel</span><span class="last">HALDEN</span></div>

<nav class="abs main-nav"><span>Home</span><span>Bio</span><span>News</span><span>Gigs</span><span>Gallery</span><span>See &amp; Hear</span><span>Store</span><span>Generosity</span><span>Contact</span></nav>

<section class="abs hero">
  <div class="hero-stage">
    <div class="hero-portrait" role="img" aria-label="Portrait of Lorel in a brown leather jacket"></div>
    <div class="hero-wall" role="img" aria-label="Dark painted brick wall"></div>
    <h1 class="hero-title">Hello EveryOne this is<br>Lorel Halden</h1>
    <div class="hero-arrow" style="left:601px"><svg width="26" height="26" viewBox="0 0 26 26"><path d="M15 7l-6 6 6 6" stroke="#333" stroke-width="3" fill="none"/></svg></div>
    <div class="hero-arrow" style="left:647px"><svg width="26" height="26" viewBox="0 0 26 26"><path d="M11 7l6 6-6 6" stroke="#333" stroke-width="3" fill="none"/></svg></div>
  </div>
</section>

<h2 class="abs welcome">Welcome to lorel Halden Official Website</h2>
<p class="abs intro">Aliquam molestie, mi et imperdiet euismod, dui purus auctor tellus, et interdum lacus lectus et ante. Sed accumsan sollicitudin sapien, sit amet adipiscing turpis gravida ac. In congue, neque ac lobortis volutpat, libero mauris varius mi, vitae suscipit ipsum ligula vitae risus. Duis aliquam nibh a dui iaculis viverra id a velit. Vivamus egestas risus in magna varius commodo. Sed semper viverra egestas.</p>
<div class="abs rule-full"></div>

<h3 class="abs section-head" style="left:97px;top:586px">Listen</h3>
<div class="abs photo" style="left:97px;top:621px;width:160px;height:87px;background:linear-gradient(90deg,#9a3b2c,#3a2a24 50%,#1d1a1a)" role="img" aria-label="Lorel singing into a microphone"></div>
<p class="abs blurb" style="left:270px;top:617px">Vestibulum vel metus sit amet turpis bibendum tincidunt vel sit amet quam. Pellentesque habitant morbi tristique senectus et...</p>
<div class="abs btn" style="left:270px;top:686px;width:76px;height:25px">PREVIEW</div>

<h3 class="abs section-head" style="left:457px;top:586px">Photo Gallery</h3>
<div class="abs photo" style="left:457px;top:621px;width:105px;height:84px;background:linear-gradient(135deg,#2a2320,#5a3a28 55%,#1a1614)" role="img" aria-label="Photo of Lorel in a dark top"></div>
<div class="abs photo" style="left:577px;top:621px;width:105px;height:84px;background:linear-gradient(90deg,#9a3b2c,#3a2a24 50%,#1d1a1a)" role="img" aria-label="Photo of Lorel singing"></div>
<div class="abs photo" style="left:697px;top:621px;width:106px;height:84px;background:linear-gradient(135deg,#1c1612,#7a4a2a 55%,#2a1a10)" role="img" aria-label="Photo of Lorel in a leather jacket"></div>

<div class="abs rule-half" style="left:97px;width:345px"></div>
<div class="abs rule-half" style="left:457px;width:346px"></div>

<h3 class="abs section-head" style="left:97px;top:729px">Store</h3>
<div class="abs photo" style="left:97px;top:763px;width:160px;height:87px;background:linear-gradient(90deg,#141210,#5a3a28 50%,#141210)" role="img" aria-label="Portrait of Lorel smiling"></div>
<p class="abs blurb" style="left:270px;top:759px">Vestibulum vel metus sit amet turpis bibendum tincidunt vel sit amet quam. Pellentesque habitant morbi tristique senectus et...</p>
<div class="abs btn" style="left:270px;top:829px;width:76px;height:25px">BUY NOW</div>

<h3 class="abs section-head" style="left:457px;top:734px">Video Gallery</h3>
<div class="abs photo" style="left:457px;top:769px;width:166px;height:83px;background:linear-gradient(90deg,#3a3a3a,#6a5a4a 55%,#2a2a2a)" role="img" aria-label="Video of Lorel playing acoustic guitar">
  <svg width="166" height="83" viewBox="0 0 166 83"><circle cx="83" cy="41" r="14" fill="#222" opacity=".8"/><path d="M79 34l10 7-10 7z" fill="#fff"/></svg>
</div>
<div class="abs photo" style="left:637px;top:769px;width:166px;height:83px;background:linear-gradient(90deg,#161616,#6a4a30 55%,#161616)" role="img" aria-label="Video of Lorel performing on stage">
  <svg width="166" height="83" viewBox="0 0 166 83"><path d="M80 34l10 7-10 7z" fill="#fff"/></svg>
</div>

<section class="abs lower"></section>

<h3 class="abs col-head" style="left:97px">Upcoming Shows</h3>
<div class="abs date-badge" style="left:97px;top:928px"><span class="mon">May</span><span class="day">20</span></div>
<p class="abs show-text" style="left:157px;top:925px">Vestibulum vel metus sit amet turpis bibendum....</p>
<span class="abs read-more" style="left:268px;top:956px">Read More</span>
<div class="abs date-badge" style="left:97px;top:1003px"><span class="mon">May</span><span class="day">18</span></div>
<p class="abs show-text" style="left:157px;top:1000px">Vestibulum vel metus sit amet turpis bibendum....</p>
<span class="abs read-more" style="left:268px;top:1031px">Read More</span>
<div class="abs btn" style="left:238px;top:1074px;width:76px;height:25px;font-size:11px">VIEW ALL</div>

<h3 class="abs col-head" style="left:345px">Recent Tweets</h3>
<div class="abs tweet-icon" style="left:350px;top:928px"></div>
<p class="abs tweet" style="left:394px;top:925px">NYC. This woman is my muse and a genius. Absolutely see this show if you can..<br><a>http://short.example/xr4bbQ</a><br><span class="ago">6 hours 37 min ago</span></p>
<div class="abs tweet-icon" style="left:350px;top:1023px"></div>
<p class="abs tweet" style="left:394px;top:1020px">NYC. This woman is my muse and a genius. Absolutely see this show if you can..<br><a>http://short.example/xr4bbQ</a><br><span class="ago">6 hours 37 min ago</span></p>

<h3 class="abs col-head" style="left:593px">Get Social</h3>
<div class="abs social-item" style="left:594px;top:925px"><div class="name">Chatterbook</div><div class="desc">Like Lorel Halden on Chatterbook.</div></div>
<div class="abs social-item" style="left:594px;top:967px"><div class="name">Chirpline</div><div class="desc">Follow Lorel Halden on Chirpline.</div></div>
<div class="abs social-item" style="left:594px;top:1009px"><div class="name">Vidplexa</div><div class="desc">Watch Lorel Halden Videos on Vidplexa.</div></div>
<div class="abs social-item" style="left:594px;top:1051px"><div class="name">Snapgrove</div><div class="desc">View Lorel Halden Pics on Snapgrove.</div></div>

<footer class="abs footer"></footer>
<p class="abs copyright">Copyright (C) 2013 LorelHalden. All Rights Reserved.</p>
<div class="abs social-dot" style="left:664px" aria-label="Chatterbook"></div>
<div class="abs social-dot" style="left:700px" aria-label="Chirpline"></div>
<div class="abs social-dot" style="left:737px" aria-label="Vidplexa"></div>
<div class="abs social-dot" style="left:773px" aria-label="Snapgrove"></div>
</body>
</html>
```